Web design for boutique law firm

Web design for law firm; practice areas include:
-international intellectual property counseling
-general corporate (contract negotiation, licensing, distribution agreements
-see my *very* outdated website at www.pvtlegalhouse.com: here is some of the home page content:

"PVT Law Group enjoys providing proactive, business-minded, efficient legal solutions for individuals and companies that benefit from major law firm experience at reasonable rates.

Some areas of emphasis include:

Counseling individuals and companies with respect to clearing, selecting, securing, managing, commercializing, and protecting intellectual property assets around the world. This includes traditional global brand management, marketing, advertising, and enforcement work as well as litigation.
PVT Law Group also provides general counseling services for individuals and businesses, from start-up advice to sophisticated business transactions strategy, agreement negotiating, dispute resolution, and litigation.
Before founding PVT Law Group in 2008, Curtis L. Abernathy led the Trademark, Copyright, & Brand Management Group for Falkner & Ingleby's Seattle office. Curtis was also a senior associate at Silicon Valley based Hartwell, Bexley, Oduya, & Penrose."

Target Market(s)

Clients/potential clients needing tier one, international intellectual property advice with "mega" law firm experience for much less than what we were/would be charging at the "mega firms".

Industry/Entity Type

Legal

Number of Pages Required

4 page

Font styles to use
Serif
Sans Serif

Colors

Designer to choose colors to be used in the design.

Requirements
Must have
• +Improvement over everything on current site at www.pvtlegalhouse.com.
• +Pictures/bios for me and my team (four of us right now).
• +Easy to update and add/remove content.
• +Must be superior in design (look, feel, ease of use, classy and elegant, but hip, reflects international practice).
• +i have logos and color schemes (see current website) but will consider improvements.
Nice to have
• Let me know your thoughts.
Should not have
• No cheese; no overt sales pitches or marketing (since law firm).

```html
<!DOCTYPE html>
<html lang="en">
<head>
<meta charset="utf-8">
<title>PVT Law Group PLLC</title>
<link href="https://fonts.googleapis.com/css2?family=Jost:wght@400;500;600&display=swap" rel="stylesheet">
<style>
:root{
  --orange:#f26a21;
  --dark:#2a2930;
  --dark-2:#34333a;
  --hero:#3b3a40;
  --light:#efede9;
  --muted:#8d8c90;
  --muted-dark:#6f6e73;
  --white:#ffffff;
  --ink:#2b2a2e;
}
*{box-sizing:border-box;margin:0;padding:0}
html,body{width:1200px;height:3529px;overflow:hidden}
body{font-family:"Jost",Arial,sans-serif;color:var(--ink);background:var(--light);position:relative}
section,header,footer{position:absolute;left:0;width:1200px;overflow:hidden}
.abs{position:absolute}
.center{left:0;width:100%;text-align:center}
.mark{width:40px;height:40px;border:2px solid var(--orange);border-radius:50%}
.vline{position:absolute;width:2px;background:var(--dark);z-index:5}

/* hero */
.hero{top:0;height:522px;background:linear-gradient(180deg,#3e3d43 0%,#35343a 60%,#2e2d33 100%)}
.hero-photo{position:absolute;inset:0;background:radial-gradient(ellipse at 55% 45%,#55535a 0%,#3b3a40 55%,#2b2a30 100%);opacity:.9}
.brand{position:absolute;left:132px;top:30px;display:flex;align-items:center;gap:10px;color:var(--white);font-size:19px;letter-spacing:.5px}
.brand .mark{width:34px;height:34px}
.brand-rule{position:absolute;left:132px;top:66px;width:206px;height:2px;background:var(--orange)}
.nav{position:absolute;top:37px;left:388px;display:flex;gap:0;font-size:14px;color:var(--white)}
.nav a{color:inherit;text-decoration:none;position:absolute;white-space:nowrap}
.nav .active{color:var(--orange);border-bottom:2px solid var(--orange);padding-bottom:5px}
.btn-cta{position:absolute;left:922px;top:31px;width:144px;height:34px;border-radius:17px;background:var(--orange);color:var(--white);font-size:14px;display:flex;align-items:center;justify-content:center}
.hero h1{top:196px;font-weight:400;font-size:30px;color:var(--white);letter-spacing:.3px}
.orange-rule{position:absolute;height:2px;background:var(--orange)}
.hero p{top:268px;font-size:16px;line-height:26px;color:#c9c8cc}
.btn-ghost{position:absolute;height:32px;border:2px solid var(--orange);border-radius:16px;color:var(--white);font-size:13px;display:flex;align-items:center;justify-content:center}
.dots{position:absolute;top:486px;left:585px;display:flex;gap:6px}
.dots i{width:7px;height:7px;border-radius:50%;background:#8a898d}
.dots i.on{background:var(--orange)}

/* welcome */
.welcome{top:522px;height:403px;background:var(--light)}
.building{position:absolute;left:682px;top:0;width:518px;height:403px;background:linear-gradient(135deg,#e2824a 0%,#f26a21 60%,#d95a16 100%)}
.person{position:absolute;left:576px;top:8px;width:200px;height:395px;background:linear-gradient(180deg,#c9b6a6 0%,#3f4a63 45%,#23252d 100%);border-radius:90px 90px 0 0}
.welcome h2{left:155px;top:100px;font-weight:400;font-size:30px}
.welcome .lead{left:155px;top:160px;width:382px;font-size:14px;line-height:20px;color:#555}
.welcome .body{left:155px;top:210px;width:382px;font-size:12.5px;line-height:18px;color:var(--muted)}
.welcome .btn-ghost{left:155px;top:327px;width:127px;color:var(--ink);font-size:13px}

/* practice */
.practice{top:925px;height:506px;background:linear-gradient(180deg,#2f2e34,#27262c)}
.sec-title{font-weight:400;font-size:28px}
.sec-sub{font-size:14px;line-height:18px;color:var(--muted)}
.practice .sec-title{color:var(--white)}
.practice .sec-sub{color:#77767b}
.pcol{position:absolute;top:230px;width:280px}
.pcol h3{font-weight:500;font-size:14px;color:var(--white);display:flex;align-items:center;gap:12px}
.pcol p{margin:18px 0 0 50px;font-size:12px;line-height:17px;color:#76757a;width:215px}
.pcol .more{display:block;margin:14px 0 0 50px;font-size:12px;color:var(--white)}
.pcol .more.hot{color:var(--orange);text-decoration:underline}
.arrow{position:absolute;color:#9c9ba0;font-size:22px}

/* attorneys */
.attorneys{top:1431px;height:588px;background:var(--light)}
.card{position:absolute;top:216px;width:280px}
.card .photo{height:278px;background:linear-gradient(180deg,var(--light) 0%,#d9d4cf 30%,#7d8fae 65%,#3a3f4c 100%)}
.card .name{height:47px;background:var(--dark);color:var(--white);font-size:14px;font-weight:500;display:flex;align-items:center;justify-content:center}
.card.featured .name{background:var(--orange)}

/* consultation */
.consult{top:2019px;height:503px;background:var(--dark)}
.office{position:absolute;left:0;top:0;width:600px;height:503px;background:linear-gradient(120deg,#cfc7bd 0%,#8e8b88 40%,#4a4c55 75%,#2e3037 100%)}
.consult .sec-title{left:661px;top:103px;color:var(--white)}
.consult .sec-sub{left:661px;top:160px;width:380px;color:#6f6e73}
.field{position:absolute;height:30px;border-bottom:1px solid #56555b;font-size:12px;color:#8b8a8f;padding-top:8px}
.send{position:absolute;left:661px;top:428px;width:146px;height:31px;border-radius:16px;background:var(--orange);color:var(--white);font-size:13px;display:flex;align-items:center;justify-content:center;gap:8px}

/* news */
.news{top:2522px;height:659px;background:var(--light)}
.ncard{position:absolute;top:231px;width:280px;height:378px;background:var(--white);border-bottom:3px solid var(--orange)}
.ncard .img{height:193px;background:linear-gradient(160deg,#b8a796 0%,#6f6660 50%,#2f2d31 100%)}
.ncard .date{margin-top:22px;text-align:center;font-size:12px;color:var(--orange)}
.ncard h4{margin:8px auto 0;width:210px;text-align:center;font-weight:500;font-size:14px;line-height:20px}
.ncard p{margin:12px auto 0;width:220px;text-align:center;font-size:12px;line-height:17px;color:var(--muted)}
.ncard.featured{background:var(--orange);border-bottom-color:var(--orange)}
.ncard.featured .date,.ncard.featured h4,.ncard.featured p{color:var(--white)}

/* footer */
.footer{top:3181px;height:348px;background:var(--dark);color:#a4a3a8}
.footer .brand{left:155px;top:42px}
.footer .brand-rule{left:155px;top:92px;width:180px}
.footer .about{left:155px;top:125px;width:235px;font-size:12.5px;line-height:17px;color:#8b8a8f}
.social{position:absolute;left:155px;top:204px;display:flex;gap:18px}
.social i{width:14px;height:14px;border-radius:50%;background:#8b8a8f}
.social i.on{background:var(--orange)}
.footer h5{position:absolute;top:76px;font-weight:500;font-size:14px;color:var(--white)}
.flink{position:absolute;font-size:12.5px;color:#8b8a8f;width:110px;padding-bottom:6px;border-bottom:1px solid #45444a}
.flink.on{color:var(--orange)}
.contact-row{position:absolute;left:762px;display:flex;gap:14px;font-size:12.5px;line-height:18px;color:#8b8a8f}
.contact-row svg{flex:none;margin-top:2px}
.footer .rule{position:absolute;left:155px;top:283px;width:887px;height:1px;background:#45444a}
.copy{position:absolute;left:155px;top:305px;font-size:12px;color:#76757a}
.top-btn{position:absolute;left:1023px;top:303px;width:20px;height:20px;border:1px solid #76757a;border-radius:50%}
</style>
</head>
<body>

<header class="hero">
  <div class="hero-photo" role="img" aria-label="Dimmed photo of business people meeting around a table"></div>
  <div class="brand"><span class="mark"></span>PVT LAW GROUP PLLC</div>
  <div class="brand-rule"></div>
  <nav class="nav">
    <a class="active" style="left:0">Home</a>
    <a style="left:73px">About</a>
    <a style="left:139px">Experience</a>
    <a style="left:238px">Practice Areas</a>
    <a style="left:358px">News</a>
    <a style="left:421px">Contact Us</a>
  </nav>
  <div class="btn-cta">Free Consultation</div>
  <h1 class="abs center">International Intellectual Property Counseling</h1>
  <div class="orange-rule" style="left:570px;top:250px;width:60px"></div>
  <p class="abs center">There are many variations of passages of Lorem Ipsum<br>available, but the majority have suffered...</p>
  <div class="btn-ghost" style="left:536px;top:340px;width:128px">Explore More</div>
  <svg class="abs" style="left:1108px;top:272px" width="56" height="40" viewBox="0 0 56 40"><line x1="2" y1="6" x2="50" y2="6" stroke="#f26a21" stroke-width="2"/><line x1="2" y1="20" x2="50" y2="20" stroke="#fff" stroke-width="2"/><line x1="2" y1="34" x2="50" y2="34" stroke="#f26a21" stroke-width="2"/></svg>
  <div class="dots"><i></i><i class="on"></i><i></i></div>
</header>
<div class="vline" style="left:173px;top:499px;height:47px"></div>

<section class="welcome">
  <div class="building" role="img" aria-label="Orange-tinted photo of a classical courthouse facade with columns"></div>
  <div class="person" role="img" aria-label="Photo of the founding attorney standing in a suit"></div>
  <div class="mark abs" style="left:155px;top:48px"></div>
  <h2 class="abs">Welcome To PVT</h2>
  <p class="abs lead">Over the years, Curtis has worked with private and public companies in numerous industries,</p>
  <p class="abs body">including consumer/retail products and services, various technology sectors (clean-technology, bio-tech, communications and networking, computer hardware and software, and electronics), telecommunications, professional and educational services, among others...</p>
  <div class="btn-ghost">Discover More</div>
</section>

<section class="practice">
  <div class="abs" style="left:0;top:0;width:1200px;height:506px;background:radial-gradient(ellipse at 50% 40%,rgba(90,88,96,.35),transparent 70%)" role="img" aria-label="Faint dark photo of a legal team at work"></div>
  <div class="mark abs" style="left:580px;top:45px"></div>
  <h2 class="abs center sec-title" style="top:100px">Practice Areas</h2>
  <p class="abs center sec-sub" style="top:155px">There are many variations of passages of Lorem Ipsum<br>available, but the majority have suffered...</p>
  <span class="arrow" style="left:92px;top:276px">&#8630;</span>
  <span class="arrow" style="left:1090px;top:276px;color:var(--orange)">&#8631;</span>

  <div class="pcol" style="left:155px">
    <h3><svg width="36" height="30" viewBox="0 0 36 30"><path d="M2 15 L18 3 L34 15 M7 12 V28 H29 V12" fill="none" stroke="#f26a21" stroke-width="3"/><rect x="14" y="17" width="8" height="11" fill="#f26a21"/></svg>Property Counseling</h3>
    <p>It is a long established fact that a reader will be distracted by the readable content...</p>
    <span class="more">Read More &raquo;</span>
  </div>
  <div class="pcol" style="left:455px">
    <h3><svg width="36" height="30" viewBox="0 0 36 30"><rect x="3" y="6" width="14" height="22" fill="#f26a21"/><rect x="19" y="12" width="14" height="16" fill="#f26a21"/><g fill="#2c2b31"><rect x="6" y="10" width="3" height="3"/><rect x="11" y="10" width="3" height="3"/><rect x="6" y="16" width="3" height="3"/><rect x="11" y="16" width="3" height="3"/><rect x="22" y="16" width="3" height="3"/><rect x="27" y="16" width="3" height="3"/></g></svg>General Corporate</h3>
    <p>It is a long established fact that a reader will be distracted by the readable content...</p>
    <span class="more hot">Read More &raquo;</span>
  </div>
  <div class="pcol" style="left:760px">
    <h3><svg width="36" height="30" viewBox="0 0 36 30"><path d="M2 12 L10 6 L18 10 L26 6 L34 12 L24 24 L18 20 L12 24 Z" fill="#f26a21"/></svg>Distribution Agreements</h3>
    <p>It is a long established fact that a reader will be distracted by the readable content...</p>
    <span class="more">Read More &raquo;</span>
  </div>
  <div class="btn-ghost" style="left:520px;top:402px;width:160px">View All Practice</div>
</section>
<div class="vline" style="left:599px;top:1407px;height:47px"></div>

<section class="attorneys">
  <div class="mark abs" style="left:580px;top:46px"></div>
  <h2 class="abs center sec-title" style="top:103px">Our Attorneys</h2>
  <p class="abs center sec-sub" style="top:155px">There are many variations of passages of Lorem Ipsum<br>available, but the majority have suffered...</p>
  <span class="arrow" style="left:92px;top:368px">&#8630;</span>
  <span class="arrow" style="left:1090px;top:368px;color:var(--orange)">&#8631;</span>
  <div class="card" style="left:155px"><div class="photo" role="img" aria-label="Portrait photo of attorney Ashley Brennan"></div><div class="name">Ashley Brennan</div></div>
  <div class="card featured" style="left:460px"><div class="photo" role="img" aria-label="Portrait photo of attorney Michael Dorran"></div><div class="name">Michael Dorran</div></div>
  <div class="card" style="left:765px"><div class="photo" role="img" aria-label="Portrait photo of attorney Rodney Calloway"></div><div class="name">Rodney Calloway</div></div>
</section>

<section class="consult">
  <div class="office" role="img" aria-label="Photo of attorneys in a meeting, one smiling in the foreground"></div>
  <div class="mark abs" style="left:661px;top:47px"></div>
  <h2 class="abs sec-title">Free Consultation</h2>
  <p class="abs sec-sub">There are many variations of passages of Lorem Ipsum<br>available, but the majority.</p>
  <div class="field" style="left:661px;top:212px;width:181px">First Name</div>
  <div class="field" style="left:859px;top:212px;width:183px">Last Name</div>
  <div class="field" style="left:661px;top:262px;width:181px">Phone</div>
  <div class="field" style="left:859px;top:262px;width:183px">Email</div>
  <div class="field" style="left:661px;top:313px;width:381px">Practice Area<span style="position:absolute;right:6px">&#8964;</span></div>
  <div class="field" style="left:661px;top:365px;width:381px;height:36px">Your Message</div>
  <div class="send"><svg width="13" height="13" viewBox="0 0 14 14"><path d="M1 7 L13 1 L9 13 L7 8 Z" fill="#fff"/></svg>Send Request</div>
</section>
<div class="vline" style="left:681px;top:1995px;height:47px;background:var(--light)"></div>
<div class="vline" style="left:599px;top:2500px;height:47px"></div>

<section class="news">
  <div class="mark abs" style="left:580px;top:48px"></div>
  <h2 class="abs center sec-title" style="top:103px">Latest News</h2>
  <p class="abs center sec-sub" style="top:156px">There are many variations of passages of Lorem Ipsum<br>available, but the majority have suffered...</p>
  <article class="ncard" style="left:155px"><div class="img" role="img" aria-label="Photo of two attorneys in robes reviewing documents"></div><div class="date">Jan-25-2017</div><h4>Contrary to popular belief, Ipsum is not simply</h4><p>including consumer/retail products and services, various technology sectors (clean-technology, bio-tech...</p></article>
  <article class="ncard featured" style="left:460px"><div class="img" role="img" aria-label="Photo of a lawyer in a library of law books"></div><div class="date">Jan-25-2017</div><h4>Contrary to popular belief, Ipsum is not simply</h4><p>including consumer/retail products and services, various technology sectors (clean-technology, bio-tech...</p></article>
  <article class="ncard" style="left:765px"><div class="img" role="img" aria-label="Photo of a courtroom hearing"></div><div class="date">Jan-25-2017</div><h4>Contrary to popular belief, Ipsum is not simply</h4><p>including consumer/retail products and services, various technology sectors (clean-technology, bio-tech...</p></article>
</section>

<footer class="footer">
  <div class="brand"><span class="mark"></span>PVT LAW GROUP PLLC</div>
  <div class="brand-rule"></div>
  <p class="abs about">There are many variations of passages of Lorem Ipsumavailable, but the majority.</p>
  <div class="social"><i></i><i class="on"></i><i></i><i></i></div>

  <h5 style="left:459px">Quick Links</h5>
  <span class="flink on" style="left:459px;top:116px">&rsaquo; Home</span>
  <span class="flink" style="left:459px;top:154px">&rsaquo; About</span>
  <span class="flink" style="left:459px;top:191px;border:0">&rsaquo; Experience</span>
  <span class="flink" style="left:612px;top:116px">&rsaquo; Practice Areas</span>
  <span class="flink" style="left:612px;top:154px">&rsaquo; News</span>
  <span class="flink" style="left:612px;top:191px;border:0">&rsaquo; Contact Us</span>

  <h5 style="left:762px">Get In Touch</h5>
  <div class="contact-row" style="top:116px"><svg width="12" height="16" viewBox="0 0 12 16"><path d="M6 1 C3 1 1 3 1 6 C1 10 6 15 6 15 C6 15 11 10 11 6 C11 3 9 1 6 1 Z" fill="none" stroke="#8b8a8f" stroke-width="1.4"/><circle cx="6" cy="6" r="2" fill="#8b8a8f"/></svg><span>240 Harbor Ave. Suite C. Seattle<br>WA. 98107</span></div>
  <div class="contact-row" style="top:160px"><svg width="12" height="14" viewBox="0 0 12 14"><path d="M2 1 L5 1 L6 4 L4 6 C5 8 6 9 8 10 L10 8 L12 9 L12 12 C12 13 11 13 10 13 C5 13 1 8 1 3 C1 2 1 1 2 1 Z" fill="#8b8a8f"/></svg><span>Phone: 206.555.0142<br>Fax: 206.555.0143</span></div>
  <div class="contact-row" style="top:205px"><svg width="14" height="11" viewBox="0 0 14 11"><rect x="1" y="1" width="12" height="9" fill="none" stroke="#8b8a8f" stroke-width="1.3"/><path d="M1 1 L7 6 L13 1" fill="none" stroke="#8b8a8f" stroke-width="1.3"/></svg><span style="text-decoration:underline">contact@pvtlawgroup.com</span></div>

  <div class="rule"></div>
  <p class="copy">&copy; 2017 PVT LAW GROUP PLLC &nbsp;|&nbsp; All Rights Reserved</p>
  <div class="top-btn"><svg width="18" height="18" viewBox="0 0 18 18"><path d="M5 11 L9 7 L13 11" fill="none" stroke="#8b8a8f" stroke-width="1.4"/></svg></div>
</footer>

</body>
</html>
```